Flyer for a company who uses pure argan oil

so we need a folder of 4 pages. including front & back.
unfolded format:
10cm wide by 6.5cm high.

Front card - as background use picture file 'front'
in the lower feathers in these languages ​​'thank you'
Thank you Bedankt Merci Danke
Shukran Grazie Tak Kop khun
Arigatô Hvala Dankie Mahalo
Please use a suitable font as on the bottle.

Back of card - as background use picture file 'back'
again in the lower springs
'Yes Kavro is here'

Inside of the folding card fitting and soft pink background.

With the following text:
Wist u dat het Kavro team alles zelf doet, van de noot tot in het flesje.
Met Kavro koopt u een 100% puur natuurproduct: volledig vrij van toevoegingen en bewaarmiddelen.
U geeft uw huid, haar, nagels de allerbeste verzorging, op elk moment van de dag!
Psoriasis, droge huid, eczeem, anti aging en zoveel meer voor heel het gezin.

''Translations of the text in English so you can understand it''
Did you know that the Kavro team does everything itself, from the nut to the bottle. With Kavro you buy a 100% pure natural product: completely free of additives and preservatives. You give your skin, hair and nails the very best care, at any time of the day! Psoriasis, dry skin, eczema, anti-aging and so much more for the whole family.

A new text with the title 'PURE HEILZAAMHEID IN ÉÉN TOPPRODUCT '
And then these 3 benefits under the title.
● Een allesomvattende dag- en nachtverzorging

● Hydraterende en egaliserende eigenschappen

● Herstellend bij huid-, haar- en nagel kwaaltjes

And then somewhere else maybe in a banner or green circle
Vegan - niet getest op dieren - 100% ongeraffineerde Argan olie

Vegan - not tested on animals - 100% unrefined Argan oil

Thanks!!

```html
<!DOCTYPE html>
<html lang="en">
<head>
<meta charset="utf-8">
<title>Kavro Argan Oil – Folding Card</title>
<link href="https://fonts.googleapis.com/css2?family=Great+Vibes&family=Poppins:wght@400;500;600;700&display=swap" rel="stylesheet">
<style>
  :root {
    --stage: #e8e8e9;
    --ink: #1c1c1c;
    --ink-soft: #4a4a4a;
    --blush: #f6dcd8;
    --blush-deep: #e9b3a8;
    --coral: #d9896f;
    --paper: #f7f5f5;
    --vegan-green: #3f9a3a;
    --vegan-green-dark: #2d7a2b;
    --white: #ffffff;
  }
  * { box-sizing: border-box; margin: 0; padding: 0; }
  html, body { width: 904px; height: 1200px; overflow: hidden; }
  body {
    background: var(--stage);
    font-family: "Poppins", sans-serif;
    color: var(--ink);
    position: relative;
  }
  .spread {
    position: absolute;
    left: 52px;
    width: 800px;
    height: 280px;
    display: flex;
    box-shadow: 0 12px 30px rgba(0,0,0,0.12);
  }
  .spread--outer { top: 170px; }
  .spread--inner { top: 720px; }
  .page {
    position: relative;
    width: 400px;
    height: 280px;
    overflow: hidden;
  }
  .page + .page { border-left: 1px solid rgba(0,0,0,0.06); }

  /* Outer pages: product photo on feathers */
  .photo {
    position: absolute; inset: 0;
    background:
      radial-gradient(ellipse 40% 55% at 80% 35%, rgba(217,137,111,0.55), transparent 70%),
      radial-gradient(ellipse 90% 45% at 50% 95%, rgba(233,179,168,0.85), transparent 75%),
      linear-gradient(180deg, var(--paper) 0%, #f4ecea 55%, var(--blush) 100%);
  }
  .photo--front {
    background:
      radial-gradient(ellipse 35% 50% at 92% 25%, rgba(217,137,111,0.5), transparent 70%),
      radial-gradient(ellipse 90% 45% at 50% 90%, rgba(233,179,168,0.85), transparent 75%),
      linear-gradient(180deg, var(--paper) 0%, #f4ecea 50%, var(--blush) 100%);
  }
  .script {
    font-family: "Great Vibes", cursive;
    font-weight: 400;
    color: var(--ink);
    line-height: 1;
  }
  .back-title {
    position: absolute; left: 0; right: 0; top: 176px;
    text-align: center; font-size: 46px;
  }
  .back-sub {
    position: absolute; left: 0; right: 0; top: 228px;
    text-align: center; font-size: 10.5px; font-weight: 600;
  }
  .front-title {
    position: absolute; left: 0; right: 0; top: 168px;
    text-align: center; font-size: 58px;
  }
  .front-languages {
    position: absolute; left: 6px; right: 6px; top: 244px;
    text-align: center; font-size: 7.6px; font-weight: 500;
    white-space: nowrap;
  }

  /* Inner pages: soft pink */
  .page--inner {
    background:
      radial-gradient(ellipse 70% 40% at 30% 90%, rgba(233,179,168,0.6), transparent 75%),
      radial-gradient(ellipse 60% 40% at 70% 10%, rgba(255,255,255,0.6), transparent 75%),
      linear-gradient(160deg, #f3d3cf 0%, var(--blush) 50%, #efc6bd 100%);
  }
  .quote-frame { position: absolute; inset: 0; }
  .quote-text {
    position: absolute; left: 52px; right: 44px; top: 56px;
    text-align: center; font-size: 9.4px; line-height: 1.65; font-weight: 500;
  }
  .quote-divider {
    width: 170px; height: 1px; background: var(--ink-soft); margin: 10px auto;
    opacity: 0.6;
  }
  .benefits {
    position: absolute; left: 26px; right: 26px; top: 44px;
  }
  .benefits-title {
    font-size: 14px; font-weight: 600; text-align: center; letter-spacing: 0.2px;
    white-space: nowrap;
    border-top: 1px solid var(--ink-soft);
    padding-top: 7px;
  }
  .benefits-list { list-style: none; margin: 8px 0 0 46px; }
  .benefits-list li {
    display: flex; align-items: center; gap: 7px;
    font-size: 9.6px; line-height: 1.9; color: var(--ink-soft);
  }
  .vegan-badge {
    position: absolute; left: 162px; top: 166px; width: 76px; height: 76px;
  }
</style>
</head>
<body>

<section class="spread spread--outer">
  <article class="page page--back">
    <div class="photo" role="img" aria-label="Product photo: small amber argan oil bottle resting on soft peach feathers"></div>
    <h2 class="back-title script">Yes Kavro is here</h2>
    <p class="back-sub">Again in the lower springs</p>
  </article>
  <article class="page page--front">
    <div class="photo photo--front" role="img" aria-label="Product photo: amber argan oil spray bottle among soft peach feathers"></div>
    <h1 class="front-title script">Thank you</h1>
    <p class="front-languages">Bedankt Merci Danke • Shukran Grazie Tak Kop khun • Arigatô Hvala Dankie Mahalo</p>
  </article>
</section>

<section class="spread spread--inner">
  <article class="page page--inner">
    <svg class="quote-frame" width="400" height="280" viewBox="0 0 400 280" aria-hidden="true">
      <path d="M72 22 H382 V222" fill="none" stroke="#2a2a2a" stroke-width="1"/>
      <path d="M30 64 V262 H322" fill="none" stroke="#2a2a2a" stroke-width="1"/>
      <text x="16" y="70" font-family="Georgia, serif" font-size="60" font-weight="700" fill="#1c1c1c">“</text>
      <text x="332" y="280" font-family="Georgia, serif" font-size="60" font-weight="700" fill="#1c1c1c">”</text>
    </svg>
    <div class="quote-text">
      <p>Did you know that the Kavro team does everything itself, from the nut to the bottle. With Kavro you buy a 100% pure natural product: completely free of additives and preservatives. You give your skin, hair and nails the very best care, at any time of the day!</p>
      <div class="quote-divider"></div>
      <p>Psoriasis, dry skin, eczema, anti-aging and so much more for the whole family.</p>
    </div>
  </article>
  <article class="page page--inner">
    <div class="benefits">
      <h2 class="benefits-title">PURE HEILZAAMHEID IN ÉÉN TOP PRODUCT</h2>
      <ul class="benefits-list">
        <li><svg width="10" height="10" viewBox="0 0 10 10" aria-hidden="true"><circle cx="5" cy="5" r="4.3" fill="none" stroke="#4a4a4a" stroke-width="0.8"/><path d="M2.8 5.1 L4.4 6.6 L7.4 3.4" fill="none" stroke="#4a4a4a" stroke-width="0.9"/></svg>Een allesomvattende dag- en nachtverzorging</li>
        <li><svg width="10" height="10" viewBox="0 0 10 10" aria-hidden="true"><circle cx="5" cy="5" r="4.3" fill="none" stroke="#4a4a4a" stroke-width="0.8"/><path d="M2.8 5.1 L4.4 6.6 L7.4 3.4" fill="none" stroke="#4a4a4a" stroke-width="0.9"/></svg>Hydraterende en egaliserende eigenschappen</li>
        <li><svg width="10" height="10" viewBox="0 0 10 10" aria-hidden="true"><circle cx="5" cy="5" r="4.3" fill="none" stroke="#4a4a4a" stroke-width="0.8"/><path d="M2.8 5.1 L4.4 6.6 L7.4 3.4" fill="none" stroke="#4a4a4a" stroke-width="0.9"/></svg>Herstellend bij huid-, haar- en nagel kwaaltjes</li>
      </ul>
    </div>
    <svg class="vegan-badge" viewBox="0 0 76 76" role="img" aria-label="Vegan, not tested on animals, 100% unrefined argan oil">
      <circle cx="38" cy="38" r="37" fill="var(--vegan-green)"/>
      <circle cx="38" cy="38" r="30" fill="none" stroke="var(--white)" stroke-width="0.8"/>
      <text x="38" y="24" text-anchor="middle" font-family="Poppins, sans-serif" font-size="6" font-weight="600" fill="#ffffff">100% unrefined</text>
      <text x="38" y="31" text-anchor="middle" font-family="Poppins, sans-serif" font-size="6" font-weight="600" fill="#ffffff">Argan oil</text>
      <text x="38" y="45" text-anchor="middle" font-family="Poppins, sans-serif" font-size="12" font-weight="600" fill="#ffffff">Vegan</text>
      <text x="38" y="54" text-anchor="middle" font-family="Poppins, sans-serif" font-size="5" font-weight="600" fill="#ffffff">not tested on animals</text>
    </svg>
  </article>
</section>

</body>
</html>
```